Glint5Gate Photography Business Cards

We need a good general business card that we can hand to our clients. We will be doing embossed gloss cards.

Target Market(s)

Real estate / Business to business / professionals

```html
<!DOCTYPE html>
<html lang="en">
<head>
<meta charset="utf-8">
<title>Glint5Gate Photography – Business Cards</title>
<link rel="stylesheet" href="https://fonts.googleapis.com/css2?family=Poppins:wght@400;500;600&display=swap">
<style>
  :root {
    --backdrop: #b6b6b6;
    --navy: #332e5c;
    --sky: #42a9df;
    --white: #ffffff;
  }
  * { margin: 0; padding: 0; box-sizing: border-box; }
  html, body {
    width: 1200px;
    height: 1200px;
    overflow: hidden;
    background: var(--backdrop);
    font-family: "Poppins", sans-serif;
  }
  .card {
    position: absolute;
    left: 250px;
    width: 700px;
    height: 400px;
    background: var(--navy);
    overflow: hidden;
  }
  .card-front { top: 170px; }
  .card-back { top: 640px; }

  .roof-art {
    position: absolute;
    inset: 0;
    width: 700px;
    height: 400px;
  }
  .front-name {
    position: absolute;
    left: 0;
    right: 0;
    top: 205px;
    text-align: center;
    color: var(--white);
    font-weight: 600;
    line-height: 1;
  }
  .front-name .name-main {
    display: block;
    font-size: 80px;
    letter-spacing: 0;
  }
  .front-name .name-sub {
    display: block;
    margin-top: 12px;
    font-size: 30px;
    letter-spacing: 11px;
    padding-left: 11px;
  }

  .badge-name {
    position: absolute;
    left: 50px;
    top: 150px;
    width: 212px;
    text-align: center;
    color: var(--white);
    font-weight: 600;
    font-size: 26px;
    line-height: 1.3;
  }

  .details {
    position: absolute;
    left: 316px;
    top: 92px;
    width: 310px;
    color: var(--white);
  }
  .details .biz-name {
    padding-left: 7px;
    font-size: 21px;
    font-weight: 600;
    line-height: 1.2;
  }
  .details .biz-line {
    padding-left: 7px;
    margin-top: 15px;
    font-size: 20px;
    font-weight: 600;
    line-height: 1.2;
  }
  .details .rule {
    margin-top: 8px;
    height: 2px;
    background: var(--sky);
  }
  .details .service {
    padding-left: 7px;
    margin-top: 9px;
    font-size: 18px;
    font-weight: 400;
  }
  .contact-list {
    list-style: none;
    margin-top: 8px;
    padding-left: 12px;
  }
  .contact-list li {
    display: flex;
    align-items: center;
    gap: 12px;
    height: 29.5px;
    font-size: 15.5px;
    font-weight: 500;
  }
  .contact-list svg {
    width: 18px;
    height: 18px;
    flex: none;
  }
  .bottom-band {
    position: absolute;
    left: 0;
    right: 0;
    bottom: 0;
    height: 17px;
    background: var(--sky);
  }
</style>
</head>
<body>

  <section class="card card-front">
    <svg class="roof-art" viewBox="0 0 700 400" aria-hidden="true">
      <rect width="700" height="400" fill="var(--sky)"/>
      <polygon points="0,231 350,31 700,231 700,400 0,400" fill="var(--white)"/>
      <polygon points="0,256 350,56 700,256 700,400 0,400" fill="var(--navy)"/>
    </svg>
    <h1 class="front-name">
      <span class="name-main">Glint5Gate</span>
      <span class="name-sub">PHOTOGRAPHY</span>
    </h1>
  </section>

  <section class="card card-back">
    <p class="badge-name">Glint5Gate<br>Photography</p>

    <div class="details">
      <p class="biz-name">Glint 5 Gate</p>
      <p class="biz-line">PHOTOGRAPHY BUSINESS</p>
      <div class="rule"></div>
      <p class="service">Photography Services</p>
      <ul class="contact-list">
        <li>
          <svg viewBox="0 0 24 24" fill="none" stroke="var(--sky)" stroke-width="1.6" stroke-linecap="round" stroke-linejoin="round" aria-hidden="true">
            <path d="M5 3h3l2 5-2.5 1.5a11 11 0 0 0 7 7L16 14l5 2v3a2 2 0 0 1-2 2A16 16 0 0 1 3 5a2 2 0 0 1 2-2z"/>
            <path d="M14 3a7 7 0 0 1 7 7M14 7a3 3 0 0 1 3 3"/>
          </svg>
          <span>0412385670</span>
        </li>
        <li>
          <svg viewBox="0 0 24 24" fill="none" stroke="var(--sky)" stroke-width="1.6" stroke-linejoin="round" aria-hidden="true">
            <rect x="2" y="5" width="20" height="14" rx="1"/>
            <path d="M2 6l10 7 10-7M2 18l7-6M22 18l-7-6"/>
          </svg>
          <span>hello@glint5gate.com</span>
        </li>
        <li>
          <svg viewBox="0 0 24 24" fill="none" stroke="var(--sky)" stroke-width="1.6" stroke-linecap="round" aria-hidden="true">
            <circle cx="12" cy="8" r="4.5"/>
            <path d="M3.5 22a8.5 8.5 0 0 1 17 0"/>
          </svg>
          <span>Lic No. 218640B</span>
        </li>
      </ul>
    </div>

    <div class="bottom-band"></div>
  </section>

</body>
</html>
```